business card for Your Loan Locator

Please create a business card for my new business. I have attached another business card i have used previously and I like its layout and the hologram style backing with the logo. Replace the information with my new business information. On the information side of the card under the logo please place the NQLA acredited member logo I have uploaded along with 'Credit Rep Number 738194'.
next to my name in smaller text and not bold write 'JP'. and my title change from director to Broker/Director
Industry/Entity Type
Mortgage Brokerage
Contact Information for Business Card
As already on the uploaded card and in project description
Colors
Designer to choose colors to be used in the design.
Look and feel
Each slider illustrates characteristics of the customer's brand and the style your logo design should communicate.

```html
<!DOCTYPE html>
<html lang="en">
<head>
<meta charset="utf-8">
<title>Your Loan Locator – Business Card</title>
<link href="https://fonts.googleapis.com/css2?family=Lato:wght@300;400;700&display=swap" rel="stylesheet">
<style>
  :root {
    --backdrop: #5f7f88;
    --card: #424242;
    --brand-blue: #1a7cc4;
    --brand-grey: #7d8896;
    --text-light: #ffffff;
    --text-soft: #e6e6e6;
    --rule: #8a8a8a;
  }
  * { margin: 0; padding: 0; box-sizing: border-box; }
  html, body { width: 1200px; height: 1200px; overflow: hidden; }
  body {
    position: relative;
    background: var(--backdrop);
    font-family: "Lato", sans-serif;
    color: var(--text-light);
  }
  .card {
    position: absolute;
    left: 180px;
    width: 840px;
    height: 480px;
    background: var(--card);
  }
  .card--front { top: 74px; }
  .card--back { top: 646px; }

  /* Front */
  .brand {
    position: absolute;
    left: 0; right: 0;
    display: flex;
    align-items: center;
    justify-content: center;
    gap: 18px;
  }
  .card--front .brand { top: 290px; }
  .brand__mark {
    width: 34px; height: 34px;
    background: var(--brand-blue);
  }
  .brand__name {
    font-weight: 400;
    font-size: 46px;
    letter-spacing: 1px;
    color: var(--brand-blue);
  }
  .site-strip {
    position: absolute;
    top: 440px;
    left: 0; right: 0;
    display: flex;
    align-items: center;
  }
  .site-strip__rule { flex: 1; height: 1px; background: var(--rule); }
  .site-strip__url {
    padding: 0 14px;
    font-size: 18px;
    font-weight: 300;
    letter-spacing: 5px;
    color: var(--text-soft);
  }

  /* Back */
  .card--back .brand {
    top: 180px;
    width: 420px;
    gap: 14px;
  }
  .card--back .brand__mark { width: 26px; height: 26px; }
  .card--back .brand__name { font-size: 32px; }
  .accreditation {
    position: absolute;
    top: 262px;
    left: 0;
    width: 420px;
    display: flex;
    align-items: center;
    justify-content: center;
    gap: 12px;
  }
  .accreditation__badge {
    width: 40px; height: 40px;
    border-radius: 50%;
    background: var(--brand-grey);
  }
  .accreditation__text {
    font-size: 16px;
    font-weight: 400;
    letter-spacing: 0.5px;
    color: var(--text-soft);
  }
  .divider {
    position: absolute;
    left: 420px; top: 50px;
    width: 1px; height: 379px;
    background: var(--rule);
  }
  .person {
    position: absolute;
    left: 466px; top: 170px;
    text-align: center;
  }
  .person__name {
    font-weight: 700;
    font-size: 30px;
    letter-spacing: -0.5px;
    padding-bottom: 4px;
    border-bottom: 1px solid var(--rule);
  }
  .person__post {
    margin-left: 6px;
    font-weight: 400;
    font-size: 18px;
    letter-spacing: 0.5px;
  }
  .person__title {
    margin-top: 4px;
    font-weight: 400;
    font-size: 19px;
    letter-spacing: 4px;
  }
  .contacts {
    position: absolute;
    left: 484px; top: 292px;
    list-style: none;
  }
  .contacts__item {
    display: flex;
    align-items: center;
    height: 44px;
    font-size: 20px;
    font-weight: 300;
    color: var(--text-soft);
  }
  .contacts__icon { width: 24px; height: 24px; margin-right: 12px; }
  .footer-rule {
    position: absolute;
    left: 0; right: 0; top: 453px;
    height: 1px;
    background: var(--rule);
  }
</style>
</head>
<body>

<section class="card card--front">
  <div class="brand">
    <span class="brand__mark"></span>
    <span class="brand__name">Your Loan Locator</span>
  </div>
  <div class="site-strip">
    <span class="site-strip__rule"></span>
    <span class="site-strip__url">www.yourloanlocator.com.au</span>
    <span class="site-strip__rule"></span>
  </div>
</section>

<section class="card card--back">
  <div class="brand">
    <span class="brand__mark"></span>
    <span class="brand__name">Your Loan Locator</span>
  </div>

  <div class="accreditation">
    <span class="accreditation__badge" role="img" aria-label="NQLA accredited member badge"></span>
    <span class="accreditation__text">Credit Rep Number 738194</span>
  </div>

  <div class="divider"></div>

  <div class="person">
    <div class="person__name">Daniel Hartley<span class="person__post">JP</span></div>
    <div class="person__title">Broker/Director</div>
  </div>

  <ul class="contacts">
    <li class="contacts__item">
      <svg class="contacts__icon" viewBox="0 0 24 24" aria-hidden="true">
        <circle cx="12" cy="12" r="12" fill="#fff"/>
        <path d="M8 5.5l2.2 3-1.4 1.6c.8 1.8 2.2 3.3 4.1 4.2l1.6-1.4 3 2.2-1.2 2.6c-5.3-.5-9.9-5-10.3-10.4z" fill="#424242"/>
      </svg>
      0400 555 018
    </li>
    <li class="contacts__item">
      <svg class="contacts__icon" viewBox="0 0 24 24" aria-hidden="true">
        <circle cx="12" cy="12" r="12" fill="#fff"/>
        <rect x="5.5" y="8" width="13" height="8.5" fill="none" stroke="#424242" stroke-width="1.3"/>
        <path d="M5.5 8l6.5 5 6.5-5M5.5 16.5l4.8-4.3M18.5 16.5l-4.8-4.3" fill="none" stroke="#424242" stroke-width="1.1"/>
      </svg>
      dan@yourloanlocator.com.au
    </li>
    <li class="contacts__item">
      <svg class="contacts__icon" viewBox="0 0 24 24" aria-hidden="true">
        <circle cx="12" cy="12" r="12" fill="#fff"/>
        <g fill="none" stroke="#424242" stroke-width="1.1">
          <circle cx="12" cy="12" r="6.5"/>
          <ellipse cx="12" cy="12" rx="3" ry="6.5"/>
          <path d="M5.5 12h13M6.5 8.7h11M6.5 15.3h11"/>
        </g>
      </svg>
      www.yourloanlocator.com.au
    </li>
  </ul>

  <div class="footer-rule"></div>
</section>

</body>
</html>
```